Business Card Design Project

I need a cool business card design for the company that will build residential houses.
The card should include:
1) Name: Boris Kalinov
2) Cell: 587.204.XXXX
3) Email: bor.kalinov@qwvend.example
4) Position: General Manager
5) Residential Home Building
6) Company logo that I have uploaded

Industry/Entity Type

Residential

```html
<!DOCTYPE html>
<html lang="en">
<head>
<meta charset="utf-8">
<title>Qwvend Developments – Business Card</title>
<link rel="stylesheet" href="https://fonts.googleapis.com/css2?family=Open+Sans:wght@400;600;700&display=swap">
<style>
  :root {
    --page-bg: #e6e7e9;
    --card-bg: #ffffff;
    --brand-blue: #1f5fae;
    --brand-green: #6fbf2a;
    --text-grey: #6f7378;
    --tag-grey: #8a8d91;
    --card-shadow: rgba(0, 0, 0, 0.16);
  }
  * { box-sizing: border-box; margin: 0; padding: 0; }
  html, body { width: 1200px; height: 900px; overflow: hidden; }
  body {
    background: var(--page-bg);
    font-family: "Open Sans", Arial, sans-serif;
    display: flex;
    flex-direction: column;
    align-items: center;
    justify-content: center;
    gap: 44px;
  }
  .card {
    width: 630px;
    height: 360px;
    background: var(--card-bg);
    box-shadow: 0 10px 30px var(--card-shadow);
    position: relative;
  }
  .card--back {
    display: flex;
    align-items: center;
    justify-content: center;
  }
  .wordmark {
    display: flex;
    align-items: center;
    color: var(--brand-blue);
    font-weight: 700;
    line-height: 1;
    white-space: nowrap;
  }
  .wordmark__dot {
    border-radius: 50%;
    background: var(--brand-green);
    flex: none;
  }
  .card--back .wordmark { font-size: 46px; gap: 18px; }
  .card--back .wordmark__dot { width: 34px; height: 34px; }

  .card--front .wordmark {
    position: absolute;
    left: 44px; top: 64px;
    font-size: 28px;
    gap: 12px;
  }
  .card--front .wordmark__dot { width: 24px; height: 24px; }

  .contact {
    position: absolute;
    left: 336px; top: 142px;
  }
  .contact__name {
    font-size: 27px;
    font-weight: 400;
    line-height: 1.2;
    color: var(--brand-blue);
  }
  .contact__role {
    font-size: 13px;
    color: var(--text-grey);
    margin: 4px 0 12px;
  }
  .contact__line {
    font-size: 13px;
    color: var(--text-grey);
    line-height: 1.65;
    white-space: nowrap;
  }
  .contact__label {
    font-weight: 700;
    color: var(--brand-blue);
    display: inline-block;
    width: 16px;
  }
  .tagline {
    position: absolute;
    left: 44px; bottom: 44px;
    font-size: 15px;
    letter-spacing: 0.5em;
    color: var(--tag-grey);
    text-transform: uppercase;
    white-space: nowrap;
  }
</style>
</head>
<body>
  <section class="card card--back" aria-label="Card back">
    <div class="wordmark"><span class="wordmark__dot"></span>Qwvend Developments</div>
  </section>

  <section class="card card--front" aria-label="Card front">
    <div class="wordmark"><span class="wordmark__dot"></span>Qwvend Developments</div>
    <div class="contact">
      <h1 class="contact__name">Boris Kalinov</h1>
      <p class="contact__role">General Manager</p>
      <p class="contact__line"><span class="contact__label">m</span>587.204.XXXX</p>
      <p class="contact__line"><span class="contact__label">e</span>bor.kalinov@qwvend.example</p>
    </div>
    <p class="tagline">Residential Home Building</p>
  </section>
</body>
</html>
```